K.T.Cash Point Business Card

We need a bi-lingual card (spanish/english). Information should be name, hours, services and address/phone. I am including a flyer as a reference--much of the information is included on it (spanish/english as well). THE COMPANY IS CALLED "K.T. CASH POINT" AND WE THINK THAT "K.T." SHOULD SUFFICE AS A LOGO--BUT WE DON'T HAVE THAT FONT NAILED DOWN. Colors should be Green/Blue scale. Happy colors. It's a check cashing business.

```html
<!DOCTYPE html>
<html lang="en">
<head>
<meta charset="utf-8">
<title>K.T. Cash Point Business Card</title>
<link href="https://fonts.googleapis.com/css2?family=Bowlby+One&display=swap" rel="stylesheet">
<style>
  :root{
    --page:#2b2b2b;
    --sky-light:#ffffff;
    --sky-mid:#bfe6fb;
    --sky-deep:#5cc3f0;
    --red:#d7202b;
    --ink:#111111;
    --green:#1f9a48;
    --purple:#4b3a9c;
    --cash-light:#dfe6cf;
    --cash-mid:#9fb08a;
    --cash-dark:#5f7356;
    --skin:#e9b89a;
  }
  *{box-sizing:border-box;margin:0;padding:0}
  html,body{width:1200px;height:900px;overflow:hidden}
  body{background:var(--page);font-family:"Bowlby One",sans-serif;position:relative}
  .card{
    position:absolute;left:240px;width:720px;height:410px;border-radius:26px;overflow:hidden;
    background:radial-gradient(ellipse 60% 70% at 45% 55%,var(--sky-light) 0%,var(--sky-mid) 45%,var(--sky-deep) 100%);
    box-shadow:0 10px 30px rgba(0,0,0,.45);
  }
  .card--front{top:25px}
  .card--back{top:465px}
  .cash{position:absolute;border-radius:40%}
  .cash--left{left:-50px;top:150px;width:160px;height:300px;
    background:radial-gradient(ellipse at 50% 50%,var(--cash-light) 0%,var(--cash-mid) 55%,rgba(159,176,138,0) 75%)}
  .cash--top{left:565px;top:-40px;width:190px;height:140px;
    background:radial-gradient(ellipse at 50% 50%,var(--cash-light) 0%,var(--cash-mid) 55%,rgba(159,176,138,0) 75%)}
  .cash--fan{left:570px;top:150px;width:110px;height:120px;border-radius:30%;
    background:radial-gradient(ellipse at 45% 50%,var(--cash-light) 0%,var(--cash-dark) 70%,rgba(95,115,86,0) 78%)}
  .hand{position:absolute;left:650px;top:160px;width:80px;height:66px;border-radius:40% 10% 10% 40%;
    background:linear-gradient(90deg,var(--skin),#f3d2bd)}
  .content{position:absolute;left:130px;top:85px;width:420px;text-align:center;white-space:nowrap;
    transform:rotate(-8deg);transform-origin:center}
  .card--back .content{top:75px}
  .brand{display:flex;align-items:center;justify-content:center;gap:10px;margin-bottom:2px}
  .brand__dot{width:26px;height:26px;border-radius:50%;background:var(--green)}
  .brand__name{font-size:20px;color:var(--purple);letter-spacing:.5px}
  .headline{font-size:40px;line-height:1.05;color:var(--red);letter-spacing:-1px;
    -webkit-text-stroke:1.5px #fff;paint-order:stroke fill;text-shadow:2px 3px 0 rgba(0,0,0,.25)}
  .card--back .headline{font-size:32px}
  .tagline{font-size:12.5px;color:var(--ink);margin-top:4px}
  .tagline--es{font-size:13px;color:var(--purple);line-height:1.2}
  .address{font-size:16px;color:var(--ink);line-height:1.15;margin-top:8px}
  .phone{display:flex;align-items:center;justify-content:center;gap:8px;font-size:26px;color:var(--green);margin-top:2px}
  .phone svg{width:22px;height:22px}
  .hours{font-size:17px;color:var(--purple);margin-top:2px}
  .spanish{font-size:13px;color:var(--red);margin-top:4px}
</style>
</head>
<body>

<section class="card card--front" aria-label="Business card, English side">
  <div class="cash cash--left" role="img" aria-label="Scattered hundred-dollar bills"></div>
  <div class="cash cash--top" role="img" aria-label="Scattered hundred-dollar bills"></div>
  <div class="cash cash--fan" role="img" aria-label="Fanned stack of dollar bills"></div>
  <div class="hand" role="img" aria-label="Hand holding the stack of bills"></div>
  <div class="content">
    <div class="brand"><span class="brand__dot"></span><span class="brand__name">K.T. CASH POINT</span></div>
    <h1 class="headline">CHECK CA$HING</h1>
    <p class="tagline">ALL CHECKS WELCOME! BEST RATES IN WESTCHESTER</p>
    <p class="address">482 ORCHARD AVENUE<br>MAPLE GLEN, NY</p>
    <p class="phone"><svg viewBox="0 0 24 24"><path fill="#1f9a48" d="M6.6 10.8c1.4 2.8 3.8 5.1 6.6 6.6l2.2-2.2c.3-.3.7-.4 1-.2 1.1.4 2.3.6 3.6.6.6 0 1 .4 1 1V20c0 .6-.4 1-1 1C10.6 21 3 13.4 3 4c0-.6.4-1 1-1h3.5c.6 0 1 .4 1 1 0 1.3.2 2.5.6 3.6.1.3 0 .7-.2 1z"/></svg>(555) 214-8390</p>
    <p class="hours">MONDAY-SATURDAY, 9AM-9PM</p>
    <p class="spanish">¡SE HABLA ESPAÑOL!</p>
  </div>
</section>

<section class="card card--back" aria-label="Business card, Spanish side">
  <div class="cash cash--left" role="img" aria-label="Scattered hundred-dollar bills"></div>
  <div class="cash cash--top" role="img" aria-label="Scattered hundred-dollar bills"></div>
  <div class="cash cash--fan" role="img" aria-label="Fanned stack of dollar bills"></div>
  <div class="hand" role="img" aria-label="Hand holding the stack of bills"></div>
  <div class="content">
    <div class="brand"><span class="brand__dot"></span><span class="brand__name">K.T. CASH POINT</span></div>
    <h2 class="headline">CAMBIO DE CHEQUES</h2>
    <p class="tagline tagline--es">¡TODOS LOS CHEQUES SON BIENVENIDOS!<br>MEJORES TARIFAS IN WESTCHESTER</p>
    <p class="address">482 ORCHARD AVENUE<br>MAPLE GLEN, NY</p>
    <p class="phone"><svg viewBox="0 0 24 24"><path fill="#1f9a48" d="M6.6 10.8c1.4 2.8 3.8 5.1 6.6 6.6l2.2-2.2c.3-.3.7-.4 1-.2 1.1.4 2.3.6 3.6.6.6 0 1 .4 1 1V20c0 .6-.4 1-1 1C10.6 21 3 13.4 3 4c0-.6.4-1 1-1h3.5c.6 0 1 .4 1 1 0 1.3.2 2.5.6 3.6.1.3 0 .7-.2 1z"/></svg>(555) 214-8390</p>
    <p class="hours">DE LUNES A SÁBADO, 9AM-9PM</p>
    <p class="spanish">¡SE HABLA ESPAÑOL!</p>
  </div>
</section>

</body>
</html>
```